Brickwise Returns Online Redesign

The company needs a new online presence built that better represents who we are and what we do. Our online presence needs to be optimised for both PC, tablet and Phone usage.

Our existing site; www.brickwisereturns.com.au - this page currently forwards to one of our sales pages.
The entire site needs to be redesigned along with the sales pages /workshop and /faststart

Here are our competition:
https://www.celiamarwood.com/
http://quorvineacademy.com.au/learning-team/celia-marwood/
http://rosalindhetheridge.com.au/
www.makeoverventures.com.au/
http://bestlayoutsplaybook.com.au/

Target Market(s)

40-55 Husband and Wife with children that are busy profesionals with a family income of 150-300k PA with 2-3 kids

Industry/Entity Type

Education

Number of Pages Required

5+ page

Font styles to use
Sans Serif
Script

Colors

Designer to choose colors to be used in the design.

Requirements
Must have
• Main Page
• Events Page
• Media Page
• Past Projects
• Blog - plesae design a template blog; both individual blogs and library (i like this http://wexo.blog/)
• eBooks page
• Shopping Cart - buy eBooks, eBook Packs and courses
• eBook download page for each eBook
• Testimonials
• Event Sales Page
• 2 hr Event - currently www.brickwisereturns.com.au/workshop & /faststart & /faststartv
Nice to have
• A few different options for sales landing pages to sell the 2 hr event
• A few different blog templates - video, text, infographic etc
• The business is a Property Educatiom, Mentoring and Consulting Company
Should not have
• This is not a real estate sales business

```html
<!DOCTYPE html>
<html lang="en">
<head>
<meta charset="utf-8">
<title>Northmead, NSW – Brickwise Returns Projects</title>
<link href="https://fonts.googleapis.com/css2?family=Jost:wght@400;500&family=Cabin:wght@400&display=swap" rel="stylesheet">
<style>
  :root{
    --header-top:#3a77a3;
    --header-bottom:#2c6590;
    --hero-blue:#6a86bd;
    --panel-blue:#c6dcfb;
    --navy:#0f2c5e;
    --white:#ffffff;
    --quote-grey:#b9c4d8;
    --page:#ffffff;
  }
  *{margin:0;padding:0;box-sizing:border-box}
  html,body{width:1200px;height:1200px;overflow:hidden;background:var(--page)}
  body{position:relative;font-family:"Jost",sans-serif;color:var(--navy)}
  .abs{position:absolute}

  .site-header{left:0;top:0;width:1200px;height:88px;background:linear-gradient(180deg,var(--header-top),var(--header-bottom));border-bottom:2px solid #d7e3ef}
  .brand{left:40px;top:30px;color:var(--white);font-size:15px;font-weight:500;letter-spacing:.5px;display:flex;align-items:center;gap:7px}
  .brand-dot{width:10px;height:10px;border:2px solid var(--white);border-radius:50%}
  .nav a{position:absolute;top:36px;color:var(--white);text-decoration:none;font-size:16px;letter-spacing:.3px}
  .nav .active{left:620px;top:30px;width:83px;height:32px;border:1.5px solid var(--white);border-radius:5px;text-align:center;line-height:29px}
  .nav small{font-size:13px}

  .hero{left:0;top:89px;width:1200px;height:716px;background:var(--hero-blue)}
  .hero-title{left:78px;top:143px;font-size:34px;font-weight:400;color:var(--white);letter-spacing:.3px}
  .hero-sub{left:398px;top:156px;font-size:17px;color:var(--navy)}
  .video{left:78px;top:233px;width:544px;height:327px;background:linear-gradient(135deg,#8fa36a 0%,#3f5a2e 45%,#6c7c55 70%,#c9ccc4 100%)}
  .play{left:322px;top:388px}
  .quote-mark{left:684px;top:196px;font-size:70px;color:var(--quote-grey);font-family:"Cabin",sans-serif;line-height:1}
  .quote{left:690px;top:236px;width:432px;text-align:right;font-size:25px;line-height:31.3px;color:var(--white)}

  .project-panel{left:78px;top:619px;width:1046px;height:382px;background:var(--panel-blue)}
  .rule{left:154px;width:885px;height:1.5px;background:var(--navy)}
  .big{font-size:33px;font-weight:500;letter-spacing:.2px}
  .small-unit{font-size:21px;font-weight:400;margin-left:10px}
  .price{font-size:23px;font-weight:500}
  .label{font-size:17px}
  .desc-title{left:154px;top:823px;font-size:20px;font-weight:500}
  .desc{left:154px;top:877px;width:890px;font-family:"Cabin",sans-serif;font-size:14px;line-height:21px}
  .before-title{left:154px;top:1032px;font-size:20px;font-weight:500}
  .thumb{top:1087px;height:113px}
  .sky{background:linear-gradient(180deg,#4f93d8 0%,#b6d2ec 40%,#5a4b44 55%,#4c6e34 100%)}
  .kitchen{background:linear-gradient(180deg,#e6dcc6,#cdbd9d)}
</style>
</head>
<body>
  <header class="site-header abs">
    <div class="brand abs"><span class="brand-dot"></span>Brickwise Returns</div>
    <nav class="nav">
      <a style="left:449px">events</a>
      <a style="left:544px">media</a>
      <a class="active">projects</a>
      <a style="left:727px">blog</a>
      <a style="left:793px">ebooks</a>
      <svg class="abs" style="left:878px;top:36px" width="20" height="17" viewBox="0 0 20 17" fill="none" stroke="#fff" stroke-width="1.5"><path d="M1 3h18l-2 12H3z"/><path d="M4 7h12M5 11h10"/></svg>
      <a style="left:914px">cart <small>(0)</small></a>
      <svg class="abs" style="left:1015px;top:35px" width="21" height="21" viewBox="0 0 21 21" fill="none" stroke="#fff" stroke-width="1.5"><circle cx="10.5" cy="10.5" r="9.5"/><path d="M5.5 12c2.5-3.5 7.5-3.5 10 0"/></svg>
      <a style="left:1045px">1300 555 214</a>
    </nav>
  </header>

  <section class="hero abs"></section>
  <h1 class="hero-title abs">NORTHMEAD, NSW</h1>
  <p class="hero-sub abs">Mark &amp; Dana, 10th November Workshop</p>
  <div class="video abs" role="img" aria-label="Video still of two workshop attendees standing in a leafy front garden"></div>
  <svg class="play abs" width="56" height="56" viewBox="0 0 56 56"><circle cx="28" cy="28" r="28" fill="#1f2a22" opacity=".75"/><path d="M24 20l11 8-11 8z" fill="#fff"/></svg>
  <div class="quote-mark abs">“</div>
  <blockquote class="quote abs">I would highly recommend people come to this event, the amount of information we have found out has been amazing! We felt very comfortable going through step by step how to renovate each phase and we were very happy with the contacts we made and the people we met.</blockquote>

  <section class="project-panel abs"></section>
  <h2 class="big abs" style="left:154px;top:650px">NORTHMEAD, NSW</h2>
  <div class="big abs" style="left:608px;top:650px">$82,000 PROFIT<span class="small-unit">in 8 weeks</span></div>
  <div class="rule abs" style="top:705px"></div>
  <div class="price abs" style="left:154px;top:724px">Purchased: $865,000</div>
  <div class="label abs" style="left:154px;top:757px">Before</div>
  <div class="price abs" style="left:609px;top:724px">Sold: $1,150,000</div>
  <div class="label abs" style="left:613px;top:757px">After</div>
  <div class="rule abs" style="top:804px"></div>
  <h3 class="desc-title abs">Project Description</h3>
  <p class="desc abs">Attend this LIVE Training Event so we can show you how we’ve successfully renovated 20 properties for profit in the last 3 years alone. Make more money in 12 weeks Renovating Property than most people make in 12 months in a job! Attend this LIVE Training Event so we can show you how we’ve successfully renovated 20 properties for profit in the last 3 years alone. Make more money in 12 weeks Renovating Property than most people make in 12 months in a job!</p>

  <h3 class="before-title abs">Before</h3>
  <div class="thumb sky abs" style="left:110px;width:302px" role="img" aria-label="Before photo of the house exterior and roof"></div>
  <div class="thumb sky abs" style="left:453px;width:302px" role="img" aria-label="Before photo of the house exterior from another angle"></div>
  <div class="thumb kitchen abs" style="left:792px;width:301px" role="img" aria-label="Before photo of the dated kitchen interior"></div>
</body>
</html>
```